RM TQW PowerPoint Template Design

Looking for an eye catching and clean powerpoint template to deliver sales proposals to our clients. RM TQW is a sales and marketing representation business in the hospitality industry, Logo it attached.

```html
<!DOCTYPE html>
<html lang="en">
<head>
<meta charset="utf-8">
<title>RM TQW – Slide</title>
<link href="https://fonts.googleapis.com/css2?family=Carlito:wght@400;700&display=swap" rel="stylesheet">
<style>
  :root {
    --brand-bronze: #7d6a3e;
    --text-body: #595959;
    --footer-grey: #7a7a7a;
    --page-white: #ffffff;
  }
  * { margin: 0; padding: 0; box-sizing: border-box; }
  html, body { width: 1200px; height: 900px; overflow: hidden; background: var(--page-white); }
  .slide {
    position: relative;
    width: 1200px;
    height: 900px;
    background: var(--page-white);
    font-family: "Carlito", "Calibri", sans-serif;
  }
  .header-band { position: absolute; left: 0; top: 0; width: 1200px; height: 83px; }
  .slide-title {
    position: absolute;
    left: 27px;
    top: 18px;
    color: var(--page-white);
    font-size: 38px;
    font-weight: 700;
    line-height: 1.2;
  }
  .brand-name {
    position: absolute;
    right: 22px;
    top: 26px;
    color: var(--brand-bronze);
    font-size: 26px;
    font-weight: 700;
    letter-spacing: 1px;
  }
  .section-title {
    position: absolute;
    left: 66px;
    top: 156px;
    color: var(--brand-bronze);
    font-size: 31px;
    font-weight: 700;
  }
  .bullet-list {
    position: absolute;
    left: 130px;
    top: 231px;
    width: 1060px;
    list-style: none;
  }
  .bullet-item {
    position: relative;
    color: var(--text-body);
    font-size: 21px;
    line-height: 33px;
    margin-bottom: 37.5px;
    white-space: nowrap;
  }
  .bullet-item::before {
    content: "";
    position: absolute;
    left: -37px;
    top: 10px;
    width: 13px;
    height: 13px;
    border-radius: 50%;
    background: var(--brand-bronze);
  }
  .footer-band {
    position: absolute;
    left: 0;
    bottom: 0;
    width: 1200px;
    height: 30px;
    background: var(--footer-grey);
  }
</style>
</head>
<body>
<div class="slide">
  <svg class="header-band" viewBox="0 0 1200 83" aria-hidden="true">
    <polygon points="0,0 1088,0 1050,83 0,83" fill="var(--brand-bronze)"/>
  </svg>
  <h1 class="slide-title">Persentation Title Here</h1>
  <div class="brand-name">RM TQW</div>

  <h2 class="section-title">Bullet title Text here</h2>

  <ul class="bullet-list">
    <li class="bullet-item">Liquorice cherry chews applicake apple pie cupcake brownie bear claw gingerbread cotton candy. Bear claw<br>croissant apple pie. Croissant cake tart liquorice tart pastry. iscuit wafer sweet apple pie. Bear claw dragée<br>sweet roll gummi fruitcake soufflé sweet gummies pie fruitcake cotton candy sugar plum</li>
    <li class="bullet-item">Liquorice cherry chews applicake apple pie cupcake brownie bear claw gingerbread cotton candy. Bear claw<br>croissant apple pie. Croissant cake tart liquorice tart pastry. iscuit wafer sweet apple pie. Bear claw dragée<br>sweet roll gummi fruitcake soufflé sweet gummies pie fruitcake cotton candy sugar plum</li>
    <li class="bullet-item">Liquorice cherry chews applicake apple pie cupcake brownie bear claw gingerbread cotton candy. Bear claw<br>croissant apple pie. Croissant cake tart liquorice tart pastry. iscuit wafer sweet apple pie. Bear claw dragée<br>sweet roll gummi fruitcake soufflé sweet gummies pie fruitcake cotton candy sugar plum</li>
    <li class="bullet-item">Liquorice cherry chews applicake apple pie cupcake brownie bear claw gingerbread cotton candy. Bear claw<br>croissant apple pie. Croissant cake tart liquorice tart pastry. iscuit wafer sweet apple pie. Bear claw dragée<br>sweet roll gummi fruitcake soufflé sweet gummies pie fruitcake cotton candy sugar plum</li>
  </ul>

  <div class="footer-band"></div>
</div>
</body>
</html>
```